Bill board design For Marlowe’s Construction

Billboard Design Request
Please design the billboard to match the branding, colors, and overall feel of our website: Marlowe's Construction Website
MARLOWE’S CONSTRUCTION
CONCRETE BUILT FOR GENERATIONS
⭐ 5-Star Rated on Zorvix
Please Include:
* All three attached project photos
* Company logo(s)
* Phone Number: 555-214-7630
* Website: MarlowesConstruction.example
* Zorvix logo with 5-star rating graphic
* Chatterly logo
* Pixtoria logo
Service Area:
Kalamazoo • Battle Creek • Coldwater • Grand Rapids
Please arrange the photos and layout in whatever way creates the strongest visual impact and readability from the road. The company name, headline, phone number, and website should be highly visible at highway speeds.
The overall appearance should be clean, professional, premium, and consistent with our website branding while highlighting our reputation, craftsmanship, and quality concrete work.
People Driving By
Concrete Construction

```html
<!DOCTYPE html>
<html lang="en">
<head>
<meta charset="utf-8">
<title>Marlowe’s Construction Billboard</title>
<link rel="stylesheet" href="https://fonts.googleapis.com/css2?family=Oswald:wght@500;600;700&family=Montserrat:wght@500;700;800&display=swap">
<style>
  :root {
    --page: #e9e9ea;
    --ink: #0b0c0e;
    --panel: #111214;
    --blue: #1a6fe0;
    --blue-bright: #2b8cff;
    --blue-deep: #0c3f9a;
    --silver: #e6e7ea;
    --grey: #c9cbcf;
    --band: #eeeff1;
    --city: #17181b;
    --star: #f6b500;
  }
  * { box-sizing: border-box; margin: 0; padding: 0; }
  html, body { width: 1200px; height: 643px; overflow: hidden; background: var(--page); }
  .billboard {
    position: absolute; left: 0; top: 51px;
    width: 1200px; height: 541px;
    background: var(--panel);
    font-family: "Oswald", sans-serif;
  }
  .stage { position: absolute; left: 0; top: 0; width: 1200px; height: 438px; }
  .stage svg { position: absolute; inset: 0; }

  .brand { position: absolute; left: 32px; top: 0; width: 370px; }
  .brand-mark {
    position: absolute; left: 140px; top: 40px;
    width: 72px; height: 72px; background: var(--blue);
  }
  .brand-name {
    position: absolute; left: 11px; top: 143px;
    font-family: "Montserrat", sans-serif; font-weight: 800;
    font-size: 45px; line-height: 1; color: var(--blue-bright);
    letter-spacing: 0.5px;
  }
  .brand-sub {
    position: absolute; left: 15px; top: 199px;
    font-family: "Montserrat", sans-serif; font-weight: 500;
    font-size: 18px; line-height: 1; color: var(--silver);
    letter-spacing: 4.1px;
  }
  .rule { position: absolute; height: 2px; background: var(--blue); }
  .rule-top { left: 14px; top: 226px; width: 344px; }
  .rule-bottom { left: 0; top: 338px; width: 338px; }
  .headline {
    position: absolute; left: 16px; top: 228px;
    font-weight: 700; font-size: 66px; line-height: 1;
    color: var(--silver); letter-spacing: 1px;
  }
  .tagline {
    position: absolute; left: 16px; top: 300px;
    font-weight: 600; font-size: 30px; line-height: 1;
    color: var(--grey); letter-spacing: 0.3px;
  }

  .phone {
    position: absolute; left: 888px; top: 334px;
    font-weight: 700; font-size: 44px; line-height: 1;
    color: #fff; letter-spacing: 0.5px;
  }
  .website {
    position: absolute; left: 763px; top: 399px;
    font-family: "Montserrat", sans-serif; font-weight: 700;
    font-size: 25px; line-height: 1; color: #fff;
  }

  .service-band {
    position: absolute; left: 0; top: 438px; width: 1200px; height: 78px;
    background: var(--band);
  }
  .cities {
    position: absolute; left: 92px; top: 24px;
    display: flex; align-items: center;
    font-weight: 600; font-size: 25px; line-height: 1; color: var(--city);
  }
  .cities .dot {
    width: 9px; height: 9px; border-radius: 50%; background: var(--blue);
    margin: 0 34px;
  }
  .rating { position: absolute; left: 900px; top: 12px; width: 130px; }
  .rating-name {
    font-family: "Montserrat", sans-serif; font-weight: 700;
    font-size: 24px; line-height: 1; color: var(--city);
  }
  .rating-row { display: flex; align-items: center; margin-top: 6px; gap: 6px; }
  .rating-score {
    font-family: "Montserrat", sans-serif; font-weight: 700;
    font-size: 14px; color: var(--city);
  }
  .divider {
    position: absolute; left: 1043px; top: 16px; width: 2px; height: 46px;
    background: var(--city);
  }
  .social {
    position: absolute; top: 30px;
    display: flex; align-items: center; gap: 4px;
    font-family: "Montserrat", sans-serif; font-weight: 700;
    font-size: 12px; line-height: 1; color: var(--city);
  }
  .social .chip { width: 9px; height: 9px; background: var(--blue); }
  .social-chatterly { left: 1054px; }
  .social-pixtoria { left: 1130px; }

  .base-band {
    position: absolute; left: 0; top: 516px; width: 1200px; height: 25px;
    background: var(--ink); border-top: 2px solid var(--blue);
  }
</style>
</head>
<body>
<div class="billboard">
  <div class="stage">
    <svg width="1200" height="438" viewBox="0 0 1200 438">
      <defs>
        <linearGradient id="bgGrad" x1="0" y1="0" x2="1" y2="1">
          <stop offset="0" stop-color="#1b1c1f"/>
          <stop offset="1" stop-color="#060607"/>
        </linearGradient>
        <linearGradient id="drivewayGrad" x1="0" y1="0" x2="0" y2="1">
          <stop offset="0" stop-color="#5f7b3c"/>
          <stop offset="0.4" stop-color="#6b6b70"/>
          <stop offset="1" stop-color="#c7c5c0"/>
        </linearGradient>
        <linearGradient id="walkwayGrad" x1="0" y1="0" x2="0" y2="1">
          <stop offset="0" stop-color="#4f6a33"/>
          <stop offset="0.4" stop-color="#6b4a37"/>
          <stop offset="1" stop-color="#a5542c"/>
        </linearGradient>
        <linearGradient id="crewGrad" x1="0" y1="0" x2="0" y2="1">
          <stop offset="0" stop-color="#5c7a3a"/>
          <stop offset="0.5" stop-color="#3a3b3e"/>
          <stop offset="1" stop-color="#8e8c86"/>
        </linearGradient>
        <linearGradient id="bandBlue" x1="0" y1="0" x2="1" y2="0">
          <stop offset="0" stop-color="#0c3f9a"/>
          <stop offset="1" stop-color="#1a5fd0"/>
        </linearGradient>
      </defs>
      <rect class="panel-bg" width="1200" height="438" fill="url(#bgGrad)"/>

      <polygon role="img" aria-label="Photo: finished concrete driveway leading to a garage"
               points="474,0 786,0 692,438 450,438 450,417 374,417" fill="url(#drivewayGrad)"/>
      <polygon role="img" aria-label="Photo: stamped red concrete walkway to a house"
               points="786,0 1015,0 929,325 895,389 692,438" fill="url(#walkwayGrad)"/>
      <polygon role="img" aria-label="Photo: crew pouring a concrete slab"
               points="1015,0 1200,0 1200,324 929,324" fill="url(#crewGrad)"/>

      <polygon points="470,0 478,0 378,417 370,417" fill="var(--blue)"/>
      <polygon points="783,0 791,0 697,417 689,417" fill="var(--blue)"/>
      <polygon points="1012,0 1019,0 935,320 928,320" fill="var(--blue)"/>
      <rect x="450" y="415" width="240" height="4" fill="var(--blue)"/>

      <polygon points="886,324 1200,324 1200,389 873,389" fill="#0a0b0d"/>
      <polygon points="873,389 870,389 886,324 889,324" fill="var(--blue)"/>
      <polygon points="640,389 1200,389 1200,438 601,438" fill="url(#bandBlue)"/>
      <line x1="640" y1="389" x2="1200" y2="389" stroke="var(--blue-bright)" stroke-width="2"/>

      <g class="icon-phone" transform="translate(847,357)">
        <circle r="22" fill="var(--blue-bright)"/>
        <path d="M-8,-11 l5,-1 3,7 -3,3 c2,4 4,6 8,8 l3,-3 7,3 -1,5 c-1,2 -3,2 -5,2 c-10,-2 -17,-9 -19,-19 c0,-2 1,-4 2,-5z" fill="#fff"/>
      </g>
      <g class="icon-globe" transform="translate(746,414)" fill="none" stroke="#fff" stroke-width="1.6">
        <circle r="13"/>
        <ellipse rx="6" ry="13"/>
        <line x1="-13" y1="0" x2="13" y2="0"/>
        <line x1="-11" y1="-6" x2="11" y2="-6"/>
        <line x1="-11" y1="6" x2="11" y2="6"/>
        <line x1="0" y1="-13" x2="0" y2="13"/>
      </g>
    </svg>

    <div class="brand">
      <div class="brand-mark"></div>
      <div class="brand-name">MARLOWE’S</div>
      <div class="brand-sub">CONSTRUCTION L.L.C</div>
      <div class="rule rule-top"></div>
      <div class="headline">CONCRETE</div>
      <div class="tagline">BUILT FOR GENERATIONS</div>
      <div class="rule rule-bottom"></div>
    </div>

    <div class="phone">555-214-7630</div>
    <div class="website">MarlowesConstruction.example</div>
  </div>

  <div class="service-band">
    <div class="cities">
      <span>KALAMAZOO</span><span class="dot"></span>
      <span>BATTLE CREEK</span><span class="dot"></span>
      <span>COLDWATER</span><span class="dot"></span>
      <span>GRAND RAPIDS</span>
    </div>
    <div class="rating">
      <div class="rating-name">Zorvix</div>
      <div class="rating-row">
        <span class="rating-score">5.0</span>
        <svg width="90" height="16" viewBox="0 0 90 16" aria-label="Five stars">
          <defs>
            <polygon id="star" points="8,0 10,5.5 16,5.8 11.3,9.5 13,15.5 8,12 3,15.5 4.7,9.5 0,5.8 6,5.5"/>
          </defs>
          <use href="#star" x="0" fill="var(--star)"/>
          <use href="#star" x="18" fill="var(--star)"/>
          <use href="#star" x="36" fill="var(--star)"/>
          <use href="#star" x="54" fill="var(--star)"/>
          <use href="#star" x="72" fill="var(--star)"/>
        </svg>
      </div>
    </div>
    <div class="divider"></div>
    <div class="social social-chatterly"><span class="chip"></span>Chatterly</div>
    <div class="social social-pixtoria"><span class="chip"></span>Pixtoria</div>
  </div>

  <div class="base-band"></div>
</div>
</body>
</html>
```